skyROAMER Helicopter Tour WordPress Website Design

SkyROAMER (skyroamer-example.com) is a premium helicopter tour company offering scenic flights in two Florida cities: Tampa and Sarasota. We are seeking a full Wordpress website redesign that is modern, upbeat, inviting, and highly conversion‑focused. The new site should feel energetic and trustworthy, reflect the excitement of helicopter sightseeing, and maintain our recognizable SkyROAMER color palette—while updating the overall look to feel fresh, clean, and current.
The website must be SEO‑friendly, mobile‑optimized, and easy to navigate. It should highlight our 5‑star customer reviews, showcase our tours clearly, and integrate seamlessly with TripLantern for instant online booking. The design should support a premium aviation experience while remaining friendly and accessible to tourists, families, couples, and adventure seekers.

These elements are essential and must be included in the design:

Brand & UX:
- Modern, upbeat, inviting design
- SEO‑friendly structure and layout
- Easy navigation and clear user flow
- Light grey “SR” background logo watermark (as used on current site)
- Clean, aviation‑inspired typography and layout

Conversion Features:
- Instant booking above the fold (TripLantern integration)
- Live Pindle Ratings carousel
- Tour comparison table (duration, route, price, etc.)
- FAQ expandable section
- Gift Cards page (highlighted as a major offering)
- What to Expect timeline (Arrive → Check‑In → Safety Briefing → Flight → Photos)
- Weather transparency widget (clear messaging about weather‑dependent flights

Content Structure:
- Separate pages for Tampa, Sarasota, and Gender Reveal Flights
- Pilot/Team profiles with short bios
- Highlighted features:
- Doors‑Off option
- Sunset flights
- Romantic packages
- Champagne add‑ons

Colors:
Use the existing SkyROAMER palette as the foundation, but modernize it.
- Background: Clean with the light grey “SR” watermark integrated tastefully.
The overall color direction should feel bright, premium, energetic, and trustworthy

Target Market(s)

Tourists visiting Tampa or Sarasota, Families looking for memorable activities, Couples seeking romantic experiences (sunset flights, proposals, anniversaries), Adventure seekers and content creators, Locals celebrating birthdays, holidays, or special occasions, Gender reveal clients looking for a unique aerial reveal experience

Industry/Entity Type

Travel & Tourism / Aviation / Helicopter Tours / Experience‑based Activities

Requirements
Must have
• These elements are essential and must be included in the design: Brand & UX - Modern, upbeat, inviting design / SEO‑friendly structure and layout / Easy navigation and clear user flow / Light grey “SR” background logo watermark (as used on current site) / Clean, aviation‑inspired typography and layout
Nice to have
• Interactive route map showing flight paths / Subtle motion or parallax effects in hero sections / Animated icons or micro‑interactions / Social media integration (Photavia grid, ClipNest clips) / Sticky mobile booking bar / Video header or short aerial footage loop / Subtle aviation‑themed graphic elements (rotor blur, sky gradients, etc.
Should not have
• No dark, heavy, or overly moody themes / No outdated fonts or overly playful typography / No cluttered layouts or excessive text blocks / No stocky, generic tourism imagery / No slow‑loading animations or heavy effects that hurt SEO

```html
<!DOCTYPE html>
<html lang="en">
<head>
<meta charset="utf-8">
<title>SkyROAMER — Scenic Helicopter Tours in Florida</title>
<link rel="stylesheet" href="https://fonts.googleapis.com/css2?family=Rubik:wght@500;600&family=Mulish:wght@400;500&display=swap">
<style>
  :root {
    --ink: #0d0e10;
    --bar: #15171a;
    --city-grey: #4a5257;
    --city-light: #6f7a80;
    --cabin-teal: #2f7580;
    --sky-warm: #c09077;
    --cabin-light: #b4c0c6;
    --white: #ffffff;
    --muted: #d3d7da;
    --divider: rgba(255,255,255,0.22);
    --brand-blue: #1846b8;
    --photo-dark: #2a2521;
    --photo-warm: #8a6a55;
  }
  * { margin: 0; padding: 0; box-sizing: border-box; }
  html, body { width: 1200px; height: 1050px; overflow: hidden; background: var(--white); }
  body { position: relative; font-family: "Mulish", sans-serif; color: var(--white); }

  .site-header { position: absolute; inset: 0 0 auto 0; z-index: 3; }
  .top-bar {
    height: 50px; background: var(--bar);
    border-bottom: 1px solid var(--divider);
    display: flex; align-items: center; justify-content: space-between;
    padding: 0 130px 0 132px; font-size: 10px; color: var(--muted);
  }
  .top-bar__contacts { display: flex; gap: 30px; align-items: center; }
  .top-bar__item { display: flex; align-items: center; gap: 7px; }
  .top-bar__item svg { width: 15px; height: 15px; stroke: var(--muted); fill: none; stroke-width: 1.4; }

  .main-nav {
    display: flex; align-items: center; justify-content: space-between;
    padding: 24px 130px 0 132px;
  }
  .brand { display: flex; align-items: center; gap: 10px; font-family: "Rubik", sans-serif; font-weight: 500; font-size: 21px; letter-spacing: 0.5px; color: var(--white); }
  .brand__mark { width: 14px; height: 14px; background: var(--white); }
  .nav-links { display: flex; align-items: center; list-style: none; font-family: "Rubik", sans-serif; font-weight: 500; font-size: 12px; }
  .nav-links li { margin-left: 36px; }
  .nav-links .btn-book {
    background: var(--white); color: var(--ink);
    padding: 11px 28px; margin-left: 2px; display: inline-block;
  }

  .hero {
    position: absolute; top: 0; left: 0; width: 1200px; height: 631px;
    background:
      radial-gradient(ellipse 300px 260px at 920px 330px, rgba(192,144,119,0.85) 0%, rgba(192,144,119,0) 100%),
      linear-gradient(100deg, var(--city-grey) 0%, var(--city-light) 38%, var(--cabin-teal) 62%, var(--sky-warm) 80%, var(--cabin-light) 100%);
  }
  .hero__photo { position: absolute; inset: 0; background: linear-gradient(90deg, rgba(10,12,14,0.62) 0%, rgba(10,12,14,0.35) 45%, rgba(10,12,14,0) 68%); }
  .hero__content { position: absolute; left: 144px; top: 235px; width: 440px; z-index: 2; }
  .hero__eyebrow { font-family: "Rubik", sans-serif; font-weight: 500; font-size: 14px; margin-left: 33px; margin-bottom: 22px; }
  .hero__title { font-family: "Rubik", sans-serif; font-weight: 600; font-size: 40px; line-height: 63px; }
  .hero__text { font-size: 13px; line-height: 23px; color: var(--muted); margin-top: -4px; width: 410px; }
  .hero__cta {
    display: inline-block; margin-top: 32px; background: var(--white); color: var(--ink);
    font-family: "Rubik", sans-serif; font-weight: 500; font-size: 12px; padding: 11px 15px;
  }

  .intro { position: absolute; top: 631px; left: 0; width: 1200px; height: 419px; background: var(--white); }
  .intro__accent { position: absolute; left: 137px; top: 73px; width: 176px; height: 346px; background: var(--brand-blue); }
  .intro__photo {
    position: absolute; left: 150px; top: 90px; width: 397px; height: 329px;
    background: linear-gradient(90deg, var(--photo-warm) 0%, var(--photo-dark) 60%, #15171a 100%);
  }
</style>
</head>
<body>
  <section class="hero">
    <div class="hero__photo" role="img" aria-label="Photo of smiling passengers wearing headsets inside a helicopter flying over downtown Tampa"></div>
    <div class="hero__content">
      <p class="hero__eyebrow">Scenic Helicopter Tours in Florida</p>
      <h1 class="hero__title">Experience<br>Florida From the Sky</h1>
      <p class="hero__text">Premium helicopter tours over Tampa and Sarasota, designed for unforgettable views, special moments, and once-in-a-lifetime experiences.</p>
      <a class="hero__cta">Book Your Flight</a>
    </div>
  </section>

  <header class="site-header">
    <div class="top-bar">
      <span>See Tampa &amp; Sarasota From the Sky</span>
      <div class="top-bar__contacts">
        <span class="top-bar__item">
          <svg viewBox="0 0 16 16"><rect x="1.5" y="3.5" width="13" height="9" rx="1"/><path d="M1.5 4l6.5 5 6.5-5"/></svg>
          info@skyroamer-example.com
        </span>
        <span class="top-bar__item">
          <svg viewBox="0 0 16 16"><path d="M4 1.8l2.2 3-1.3 1.6c.8 1.8 2.2 3.2 4 4l1.6-1.3 3 2.2-1.2 2.2c-5.5-.3-10-4.8-10.3-10.3z"/></svg>
          (555) 014-2290
        </span>
      </div>
    </div>
    <nav class="main-nav">
      <div class="brand"><span class="brand__mark"></span>SkyROAMER</div>
      <ul class="nav-links">
        <li>Tours</li>
        <li>Tampa</li>
        <li>Sarasota</li>
        <li>Gift Cards</li>
        <li>Reviews</li>
        <li>FAQ</li>
        <li><a class="btn-book">Book Now</a></li>
      </ul>
    </nav>
  </header>

  <section class="intro">
    <div class="intro__accent"></div>
    <div class="intro__photo" role="img" aria-label="Close-up photo of passengers inside the helicopter cabin"></div>
  </section>
</body>
</html>
```